Food humor T-shirt and apparel company needs a Shopfront site designed. We have logo files to help.

We are an apparel company based in Chicago by two cooking and food humor enthusiasts. We are looking for a redesign of our Shopfront site. Our products are humorous quotes and pictures on shirts, sweaters and other apparel. The tagline for the company is - Find Your Yum. Wear Your Food. We want to see designs that incorporate our logo, brand color of royal purple, signify fun business casual clothing with amusing tags or images of trendy or esoteric food trends. The design should communicate excellence in taste but with maybe a satirical almost corporate type spin.
Target Market(s)
Hip, millennial foodies and cooks that love to try new foods, have great taste, and love to experiment in the restaurant or the kitchen.
Industry/Entity Type
Cooking
Look and feel

```html
<!DOCTYPE html>
<html lang="en">
<head>
<meta charset="utf-8">
<title>Savorine — Find Your Yum. Wear Your Food.</title>
<link href="https://fonts.googleapis.com/css2?family=Playfair+Display:wght@700;900&family=Mulish:wght@400;600;700&display=swap" rel="stylesheet">
<style>
:root{
  --purple:#6a3d9a;
  --purple-dark:#4b2a7b;
  --navy:#2a2f86;
  --link-blue:#2e5cb8;
  --ink:#2b2b2b;
  --muted:#666;
  --hero-bg:#efedf6;
  --gray-band:#f2f2f2;
  --footer:#0b4fa8;
  --line:#e4e4e4;
  --white:#fff;
}
*{margin:0;padding:0;box-sizing:border-box}
html,body{width:1200px;height:3659px;overflow:hidden}
body{position:relative;background:var(--white);font-family:"Mulish",sans-serif;color:var(--ink)}
.abs{position:absolute}
.serif{font-family:"Playfair Display",serif}

/* header */
.site-header{position:absolute;left:0;top:0;width:1200px;height:160px}
.call-us{left:83px;top:48px;font-size:15px;display:flex;align-items:center;gap:8px}
.brand{left:0;width:1200px;top:30px;display:flex;justify-content:center;align-items:center;gap:10px;flex-direction:column}
.brand-mark{width:22px;height:22px;border-radius:50%;background:var(--purple)}
.brand-name{font-family:"Playfair Display",serif;font-weight:700;font-size:30px;color:var(--purple)}
.header-icons{right:100px;top:42px;display:flex;gap:26px}
.main-nav{left:0;width:1200px;top:122px;display:flex;justify-content:center;gap:40px;font-size:13px}
.main-nav a{color:var(--ink);text-decoration:none}
.main-nav a.active{color:var(--purple)}

/* hero */
.hero{left:0;top:161px;width:1200px;height:559px;background:var(--hero-bg)}
.hero-tagline{left:122px;top:155px;font-size:24px;letter-spacing:.5px;color:#333}
.hero-title{left:84px;top:205px;width:520px;text-align:center;font-size:50px;line-height:58px;color:var(--purple);font-weight:700}
.btn{display:inline-flex;align-items:center;justify-content:center;font-size:12px;font-weight:700;text-transform:uppercase;color:var(--white);background:var(--purple);border:2px solid #c9b7e0;box-shadow:0 0 0 1px var(--purple)}
.hero-btn{left:227px;top:349px;width:119px;height:48px}
.hero-photo{left:707px;top:0;width:493px;height:559px;background:linear-gradient(135deg,#8fd4e0 0%,#3fa7c4 40%,#e8e4ea 70%,#cfc7d6 100%)}

/* about */
.about-block{left:166px;top:854px;width:478px;height:395px;background:var(--purple)}
.about-photo{left:134px;top:817px;width:476px;height:395px;background:linear-gradient(160deg,#d8cfc4,#8a7f74 55%,#4c4540)}
.about-rule{left:93px;top:817px;width:1px;height:70px;background:#555}
.about-side{left:60px;top:1010px;transform:rotate(-90deg);transform-origin:left top;font-size:13px;letter-spacing:4px;color:#444;font-weight:600;white-space:nowrap;left:84px;top:1140px}
.about-title{left:741px;top:900px;font-size:32px;color:var(--navy);font-weight:700}
.about-text{left:741px;top:953px;width:385px;font-size:13.5px;line-height:24px;color:#444}
.about-btn{left:741px;top:1080px;width:118px;height:47px}

/* products */
.section-title{font-family:"Playfair Display",serif;font-weight:700;color:var(--navy);font-size:32px}
.products-title{left:83px;top:1328px;letter-spacing:1px}
.filters{left:729px;top:1348px;font-size:12px;display:flex;gap:14px;color:#333}
.filters .current{color:var(--link-blue)}
.promo{left:83px;top:1402px;width:400px;height:720px;background:linear-gradient(180deg,#3b8ac4,#2f6fa8 60%,#1d4e80)}
.promo-label{left:83px;top:1781px;width:200px;height:42px;background:var(--white);display:flex;align-items:center;padding-left:18px;font-size:14px;font-weight:700;color:var(--navy)}
.promo-text{left:100px;top:1840px;width:370px;font-size:12.5px;line-height:22px;color:var(--white)}
.promo-btn{left:100px;top:1900px;width:115px;height:32px;background:var(--purple);color:var(--white);font-size:13px;display:flex;align-items:center;justify-content:center}
.product-card{width:290px;height:362px;background:var(--white);box-shadow:0 1px 6px rgba(0,0,0,.12)}
.product-card .wish{position:absolute;right:14px;top:12px}
.product-shot{position:absolute;left:50%;transform:translateX(-50%);top:28px;width:190px;height:210px}
.product-name{position:absolute;left:0;width:100%;top:250px;text-align:center;font-size:14px;color:#333}
.product-price{position:absolute;left:0;width:100%;top:276px;text-align:center;font-size:13px;color:var(--link-blue);font-weight:700}
.cart-btn{position:absolute;left:50%;transform:translateX(-50%);top:302px;width:120px;height:32px;border:1px solid #bbb;font-size:13px;display:flex;align-items:center;justify-content:center;color:#333;background:var(--white)}
.cart-btn.solid{background:var(--purple);border-color:var(--purple);color:var(--white)}
.swatches{position:absolute;right:28px;top:48px;display:flex;flex-direction:column;gap:6px}
.swatches span{width:12px;height:12px;border-radius:50%}
.view-more{left:539px;top:2197px;width:120px;height:47px;background:var(--purple);color:var(--white);font-size:13px;display:flex;align-items:center;justify-content:center}

/* blog */
.blog{left:0;top:2285px;width:1200px;height:471px;background:var(--gray-band)}
.blog-title{left:0;width:1200px;text-align:center;top:85px}
.blog-arrow{width:18px;height:18px;border:1px solid #555;border-radius:50%;display:flex;align-items:center;justify-content:center}
.blog-img{width:218px;height:217px}
.blog-head{font-size:17px;font-weight:700;line-height:22px;width:240px}
.blog-date{font-size:12px;color:#444}
.blog-excerpt{font-size:12.5px;line-height:19px;color:#444;width:235px}
.read-more{width:118px;height:32px;background:var(--purple);color:var(--white);font-size:13px;display:flex;align-items:center;justify-content:center}

/* testimonial */
.quote-mark{left:0;width:1200px;text-align:center;top:2818px;font-family:"Playfair Display",serif;font-size:70px;color:var(--link-blue);line-height:70px}
.testimonial-text{left:317px;top:2885px;width:566px;text-align:center;font-size:12.5px;line-height:22px;color:#444}
.avatar{left:568px;top:3024px;width:64px;height:64px;border-radius:50%;background:radial-gradient(circle,#7d7d7d,#3a3a3a)}
.t-arrow{top:3052px;width:22px;height:22px;border:1px solid #777;border-radius:50%;display:flex;align-items:center;justify-content:center}
.person{left:0;width:1200px;text-align:center;top:3102px;font-size:16px;font-weight:700;color:var(--link-blue)}
.role{left:0;width:1200px;text-align:center;top:3128px;font-size:11px;color:#333}

/* footer */
.site-footer{left:0;top:3220px;width:1200px;height:439px;background:var(--footer);color:var(--white)}
.f-title{font-size:14px;font-weight:600}
.f-text{font-size:12px;line-height:24px}
.f-phone{font-size:18px;font-weight:600}
.newsletter-input{width:240px;height:32px;background:#8aa9d6;color:var(--white);font-size:12px;display:flex;align-items:center;padding-left:14px}
.send-btn{width:96px;height:32px;background:var(--white);color:var(--footer);font-size:13px;display:flex;align-items:center;justify-content:center}
.pay-icons,.social-icons{display:flex;gap:16px}
.pay-icons span{width:20px;height:15px;border:2px solid var(--white);border-radius:2px}
.social-icons span{width:18px;height:18px;border:2px solid var(--white);border-radius:50%}
.f-rule{left:83px;top:331px;width:1034px;height:1px;background:rgba(255,255,255,.35)}
.copyright{left:83px;top:352px;font-size:11px}
</style>
</head>
<body>

<header class="site-header">
  <div class="abs call-us">
    <svg width="15" height="15" viewBox="0 0 24 24"><path d="M6.6 10.8a15 15 0 0 0 6.6 6.6l2.2-2.2c.3-.3.7-.4 1-.2 1.1.4 2.3.6 3.6.6.6 0 1 .4 1 1V20c0 .6-.4 1-1 1A17 17 0 0 1 3 4c0-.6.4-1 1-1h3.5c.6 0 1 .4 1 1 0 1.3.2 2.5.6 3.6.1.3 0 .7-.2 1z" fill="#222"/></svg>
    Call Us : - 555.014.2290
  </div>
  <div class="abs brand">
    <span class="brand-mark"></span>
    <span class="brand-name">Savorine</span>
  </div>
  <div class="abs header-icons">
    <svg width="16" height="16" viewBox="0 0 24 24" fill="none" stroke="#222" stroke-width="2"><circle cx="10" cy="10" r="6"/><path d="M15 15l6 6"/></svg>
    <svg width="16" height="16" viewBox="0 0 24 24" fill="none" stroke="#222" stroke-width="2"><path d="M12 20s-8-5-8-11a4.5 4.5 0 0 1 8-2.6A4.5 4.5 0 0 1 20 9c0 6-8 11-8 11z"/></svg>
    <svg width="16" height="16" viewBox="0 0 24 24" fill="none" stroke="#222" stroke-width="2"><path d="M2 4h3l3 11h11l2-8H7"/><circle cx="9" cy="20" r="1.5"/><circle cx="18" cy="20" r="1.5"/></svg>
  </div>
  <nav class="abs main-nav">
    <a class="active" href="#">Home</a><a href="#">About Us</a><a href="#">Shop</a><a href="#">Blog</a><a href="#">Testimonial</a><a href="#">Contact Us</a>
  </nav>
</header>

<section class="abs hero">
  <p class="abs hero-tagline">Find Your Yum. Wear Your Food.</p>
  <h1 class="abs hero-title serif">Your style is your Characteristic</h1>
  <a class="abs btn hero-btn">Shop Now!</a>
  <div class="abs hero-photo" role="img" aria-label="Woman in glasses wearing a food-print t-shirt against a teal wall"></div>
</section>

<section class="about">
  <div class="abs about-rule"></div>
  <p class="abs about-side">PASSTION FOR PRINTING</p>
  <div class="abs about-block"></div>
  <div class="abs about-photo" role="img" aria-label="Screen printing workshop with two printers at work"></div>
  <h2 class="abs about-title serif">HELLO! SAVORINE</h2>
  <p class="abs about-text">Savorine was born from the hearts of two foodies and travelholics based in Los Angeles and Chicago. Savorine is an expression of their mutual love of and wanderlust for all things decadent, delicious, divine, and daring! So join us on a foodie lovers' journey and let us help you find your yum!</p>
  <a class="abs btn about-btn">Shop Now!</a>
</section>

<section class="products">
  <h2 class="abs section-title products-title">PRODUCT &nbsp;SAVORINE</h2>
  <div class="abs filters"><span class="current">All categories</span><span>//</span><span>T-Shirt</span><span>//</span><span>Shirts</span><span>//</span><span>Sweaters</span></div>

  <div class="abs promo" role="img" aria-label="Woman wearing a blue graphic t-shirt"></div>
  <div class="abs promo-label">DESIGN YOUR OWN</div>
  <p class="abs promo-text">Design and Order Online | Next Day Dispatch | No Minimums | Digital Printing | Free Design Support</p>
  <a class="abs promo-btn">Order Now</a>

  <article class="abs product-card" style="left:515px;top:1402px">
    <svg class="wish" width="14" height="14" viewBox="0 0 24 24" fill="none" stroke="#333" stroke-width="2"><path d="M12 20s-8-5-8-11a4.5 4.5 0 0 1 8-2.6A4.5 4.5 0 0 1 20 9c0 6-8 11-8 11z"/></svg>
    <div class="product-shot" role="img" aria-label="Black ladies' scoopneck t-shirt with food print" style="background:linear-gradient(#2a2a2a,#111)"></div>
    <div class="swatches"><span style="background:#e8175d"></span><span style="background:#1ea0e0"></span><span style="background:#2a4fb0"></span><span style="background:#111"></span><span style="background:#3aa53a"></span></div>
    <p class="product-name">Ladies' Scoopneck T-Shirt</p>
    <p class="product-price">From 30$</p>
    <a class="cart-btn solid">Add to cart</a>
  </article>
  <article class="abs product-card" style="left:837px;top:1402px">
    <svg class="wish" width="14" height="14" viewBox="0 0 24 24" fill="none" stroke="#333" stroke-width="2"><path d="M12 20s-8-5-8-11a4.5 4.5 0 0 1 8-2.6A4.5 4.5 0 0 1 20 9c0 6-8 11-8 11z"/></svg>
    <div class="product-shot" role="img" aria-label="Dark grey ladies' tank top with food print" style="background:linear-gradient(#4a4a4a,#2c2c2c)"></div>
    <p class="product-name">Ladies' Tank</p>
    <p class="product-price">From 30$</p>
    <a class="cart-btn">Add to cart</a>
  </article>
  <article class="abs product-card" style="left:515px;top:1788px;height:351px">
    <svg class="wish" width="14" height="14" viewBox="0 0 24 24" fill="none" stroke="#333" stroke-width="2"><path d="M12 20s-8-5-8-11a4.5 4.5 0 0 1 8-2.6A4.5 4.5 0 0 1 20 9c0 6-8 11-8 11z"/></svg>
    <div class="product-shot" role="img" aria-label="Black embroidered apron worn over a grey shirt" style="background:linear-gradient(#8a8178,#1d1d1d 40%)"></div>
    <p class="product-name">Embroidered Apron</p>
    <p class="product-price">From 30$</p>
    <a class="cart-btn">Add to cart</a>
  </article>
  <article class="abs product-card" style="left:837px;top:1788px;height:351px">
    <svg class="wish" width="14" height="14" viewBox="0 0 24 24" fill="none" stroke="#333" stroke-width="2"><path d="M12 20s-8-5-8-11a4.5 4.5 0 0 1 8-2.6A4.5 4.5 0 0 1 20 9c0 6-8 11-8 11z"/></svg>
    <div class="product-shot" role="img" aria-label="Black hooded sweatshirt with food print" style="background:linear-gradient(#2a2a2a,#0f0f0f)"></div>
    <p class="product-name">Hooded Swfatshirt</p>
    <p class="product-price">From 40.50$</p>
    <a class="cart-btn">Add to cart</a>
  </article>

  <a class="abs view-more">View More</a>
</section>

<section class="abs blog">
  <h2 class="abs section-title blog-title">BLOG SAVORINE</h2>
  <div class="abs blog-arrow" style="left:28px;top:260px"><svg width="8" height="8" viewBox="0 0 10 10"><path d="M7 1L3 5l4 4" stroke="#333" stroke-width="1.6" fill="none"/></svg></div>
  <div class="abs blog-arrow" style="left:1152px;top:260px"><svg width="8" height="8" viewBox="0 0 10 10"><path d="M3 1l4 4-4 4" stroke="#333" stroke-width="1.6" fill="none"/></svg></div>

  <div class="abs blog-img" style="left:83px;top:156px;background:radial-gradient(circle at 45% 60%,#c0603a,#3a1a12 60%,#0d0d0d)" role="img" aria-label="Two cocktails on a dark bar counter"></div>
  <h3 class="abs blog-head" style="left:315px;top:162px;color:var(--link-blue)">I'm Parched, Let's Drink: Juniper Lounge, North Center, Chicago</h3>
  <p class="abs blog-date" style="left:315px;top:250px">April 14, 2019</p>
  <p class="abs blog-excerpt" style="left:315px;top:276px">Show me a bartender that doesn't taste, worth your sips or your silver.</p>
  <a class="abs read-more" style="left:315px;top:340px">Read More</a>

  <div class="abs blog-img" style="left:602px;top:156px;background:radial-gradient(circle,#d9953f,#a85a1f 60%,#5c2f12)" role="img" aria-label="Lattice-topped salted caramel apple pie"></div>
  <h3 class="abs blog-head" style="left:841px;top:162px;color:#222">Salted Caramel Apple Pie Minis</h3>
  <p class="abs blog-date" style="left:841px;top:208px">April 14, 2019</p>
  <p class="abs blog-excerpt" style="left:841px;top:234px">Dearly Beloved, we are gathered here today to celebrate the union of salted caramel sauce and warm spiced apples. I present to you a recipe for a dessert marriage made</p>
  <a class="abs read-more" style="left:841px;top:340px">Read More</a>
</section>

<section class="testimonial">
  <div class="abs quote-mark">&ldquo;</div>
  <p class="abs testimonial-text">Sed ut perspiciatis unde omnis iste natus error sit voluptatem accusantium doloremque laudantium, totam rem aperiam, eaque ipsa quae ab illo inventore veritatis et quasi beatae vitae dicta sunt explicabo. Nemo enim ipsam voluptatem quia voluptas sit aspernatur aut ...</p>
  <div class="abs t-arrow" style="left:467px"><svg width="8" height="8" viewBox="0 0 10 10"><path d="M7 1L3 5l4 4" stroke="#333" stroke-width="1.6" fill="none"/></svg></div>
  <div class="abs avatar" role="img" aria-label="Portrait of the customer"></div>
  <div class="abs t-arrow" style="left:706px"><svg width="8" height="8" viewBox="0 0 10 10"><path d="M3 1l4 4-4 4" stroke="#333" stroke-width="1.6" fill="none"/></svg></div>
  <p class="abs person">Dana Morrow</p>
  <p class="abs role">Director</p>
</section>

<footer class="abs site-footer">
  <p class="abs f-title" style="left:83px;top:78px">Savorine</p>
  <p class="abs f-text" style="left:83px;top:118px">Call Us: <span class="f-phone">&#9742; 555.014.2290</span></p>
  <p class="abs f-text" style="left:83px;top:146px">hello@savorine-shop.com</p>
  <p class="abs f-text" style="left:83px;top:178px;width:230px;line-height:20px">Address:<br>P.O. Box 418, Larkspur Ave, Chicago IL 60614</p>

  <p class="abs f-title" style="left:427px;top:78px">Quick Links:</p>
  <p class="abs f-text" style="left:427px;top:112px">About Us<br>Shop<br>Blog<br>Testimonial<br>Contact Us</p>

  <p class="abs f-title" style="left:634px;top:78px">Newsletter:</p>
  <div class="abs newsletter-input" style="left:634px;top:135px">Enter Your Email...</div>
  <a class="abs send-btn" style="left:634px;top:178px">Send</a>

  <p class="abs f-title" style="left:963px;top:78px">Payment</p>
  <div class="abs pay-icons" style="left:963px;top:125px"><span></span><span></span><span></span><span></span></div>

  <div class="abs f-rule"></div>
  <p class="abs copyright">© 2019, Savorine. Powered by Shopfront</p>
  <div class="abs social-icons" style="left:963px;top:346px"><span></span><span></span><span></span><span></span></div>
</footer>

</body>
</html>
```